Business Stationary & Card Design

Double sided business cards, letterhead, horizontal brochure, and envelope design using our logo. We want a modern minimal look. One side of the business card should be only our logo and maybe our slogan "Get It Done Right". The other side should include our coil spring and not the logo again. Watermark like (or not) positioned partially, horizontal, on angle, or a combination of. IF a background color or accent color is used we like blue (4885ed). The letterhead, brochure, and envelope design should be similar to the card. Except no solid background color.Maybe the spring at the bottom of the letterhead page watermark style and partial. Additional info on the business card should be present:
Employee Name
Position
Phone
Email
Address
The final design should communicate strength, simplicity, and newness.

Target Market(s)

35-55 Male & Female

Industry/Entity Type

Automotive

Contact Information for Business Card

One side of the double sided business card should be only our logo and maybe our slogan "Get It Done Right". The other side should include our coil spring and not the logo again. Watermark like (or not) positioned partially, horizontal, on angle, or a combination of. IF a background color or accent color is used we like blue (4885ed). Additional info on the business card should be present:
Employee Name
Position
Phone
Email
Address

Font styles to use
Other font styles liked:
• Use font that compliments the attached font. Maybe plain eurostyle?

Colors
0492cd
3276b5

Requirements
Must have
• Use the coil spring in a subtle unique way (s). Double sided business card
Should not have
• Clutter, colors that do not coordinate well with our logo. Fonts that do not compliment our font.

```html
<!DOCTYPE html>
<html lang="en">
<head>
<meta charset="utf-8">
<title>Torsa Motion – Double Sided Business Card</title>
<link rel="stylesheet" href="https://fonts.googleapis.com/css2?family=Michroma&family=Open+Sans:wght@700&display=swap">
<style>
  :root {
    --page-bg: #d2d2d2;
    --header-bg: #ececec;
    --header-ink: #1f2d5c;
    --card-bg: #f6f6f4;
    --ink: #1e1e1e;
    --accent: #dcb623;
    --watermark: #9a9a9a;
    --rule: #222;
  }
  * { margin: 0; padding: 0; box-sizing: border-box; }
  html, body { width: 1200px; height: 1200px; overflow: hidden; }
  body { background: var(--page-bg); font-family: "Michroma", sans-serif; position: relative; }

  .board-header {
    height: 126px; background: var(--header-bg); border-bottom: 2px solid #222;
    text-align: center; font-family: "Open Sans", sans-serif; font-weight: 700; color: var(--header-ink);
    padding-top: 18px;
  }
  .board-header__title { font-size: 24px; letter-spacing: 5px; }
  .board-header__sub { font-size: 17px; letter-spacing: 3.6px; margin-top: 10px; }

  .card {
    position: absolute; width: 740px; height: 422px; background: var(--card-bg);
    box-shadow: 0 14px 28px rgba(0,0,0,.18); overflow: hidden;
  }
  .card--info { left: 70px; top: 180px; }
  .card--brand { left: 390px; top: 720px; }

  .card__watermark {
    position: absolute; right: -60px; top: -40px; width: 300px; height: 300px;
    background: linear-gradient(135deg, var(--watermark), rgba(154,154,154,.55));
    border-radius: 40px; transform: rotate(-24deg); opacity: .9;
  }
  .person { position: absolute; left: 56px; top: 120px; }
  .person__name { font-size: 30px; color: var(--ink); font-weight: 400; letter-spacing: 1px; -webkit-text-stroke: .8px var(--ink); }
  .person__role { font-size: 12px; color: var(--accent); margin-top: 6px; letter-spacing: .5px; }

  .contact { position: absolute; left: 56px; bottom: 56px; list-style: none; font-size: 12px; color: var(--ink); line-height: 2.1; }
  .contact__label { color: var(--accent); margin-right: 8px; }

  .brand { position: absolute; left: 0; right: 0; top: 126px; text-align: center; }
  .brand__name { font-size: 44px; color: var(--accent); letter-spacing: 2px; display: inline-block; }
  .brand__rule { display: block; width: 420px; height: 3px; background: var(--rule); margin: 14px auto 0; }
  .brand__slogan {
    position: absolute; left: 0; right: 0; bottom: 70px; text-align: center;
    font-size: 16px; color: var(--ink); letter-spacing: 2px; -webkit-text-stroke: .5px var(--ink);
  }
</style>
</head>
<body>
  <header class="board-header">
    <h1 class="board-header__title">DOUBLE SIDED BUSINESS CARD</h1>
    <p class="board-header__sub">RECTANGULAR SHAPE, ROUNDED SHAPE AVAILABLE</p>
  </header>

  <section class="card card--info">
    <div class="card__watermark" role="img" aria-label="Partial coil spring watermark in grey"></div>
    <div class="person">
      <h2 class="person__name">MARCO DELUCA</h2>
      <p class="person__role">Director of Marketing</p>
    </div>
    <ul class="contact">
      <li><span class="contact__label">P :</span>+33(0)4 12 34 56 78</li>
      <li><span class="contact__label">E :</span>marco.deluca@torsamotion.com</li>
      <li><span class="contact__label">A :</span>14 Rue des Lilas 75011 Paris</li>
    </ul>
  </section>

  <section class="card card--brand">
    <div class="brand">
      <span class="brand__name">TORSA MOTION</span>
      <span class="brand__rule"></span>
    </div>
    <p class="brand__slogan">GET IT DONE RIGHT</p>
  </section>
</body>
</html>
```